Updated Stationary needed using new logo for Hair Tissue Mineral Analysis Company

Simple stationary design needed using new logo!
1. 8.5" x 11" Letterhead with company information listed below
2. 8.5" x 11" Design with Footer only with logo and information for print materials
3. 5.5" x 8.5" letterhead design
4. 4.125" x 9.5" Business envelope (#10 envelope) with address
5. 4.125" x 9.5" Business envelope with clear window (#10 envelope) with address
6. 6.5" x 9.5" envelope (6 3/4 Booklet envelope) with address
7. 10" x 13" Open End envelope
Address:
4817 N. Corwin Street
Phoenix, AZ 85021
Phone:
(602)-417-3926
Website:
www.pexumor.com
Email:
information@pexumor.com
Updates
Need extra days to review
Focused on completing other projects first
Look and feel
Each slider illustrates characteristics of the customer's brand and the style your logo design should communicate.

```html
<!DOCTYPE html>
<html lang="en">
<head>
<meta charset="utf-8">
<title>Pexumor Labs Letterhead</title>
<link href="https://fonts.googleapis.com/css2?family=Figtree:wght@400;600;700&display=swap" rel="stylesheet">
<style>
  :root {
    --backdrop: #e0e0e0;
    --paper: #ffffff;
    --brand-blue: #2c559c;
    --brand-orange: #f58a26;
    --ink: #2b2b2b;
    --ink-soft: #666666;
    --sig-tone: #ececec;
  }
  * { margin: 0; padding: 0; box-sizing: border-box; }
  html, body {
    width: 1200px; height: 1200px; overflow: hidden;
    background: var(--backdrop);
    font-family: "Figtree", Arial, sans-serif;
  }
  .letterhead {
    position: absolute; left: 216px; top: 76px;
    width: 768px; height: 1046px;
    background: var(--paper);
    overflow: hidden;
  }
  .brand {
    position: absolute; left: 0; right: 0; top: 58px;
    display: flex; justify-content: center; align-items: center; gap: 10px;
  }
  .brand-mark {
    width: 22px; height: 22px; border-radius: 50%;
    background: var(--brand-orange);
  }
  .brand-name {
    font-weight: 700; font-size: 34px; letter-spacing: 2px;
    color: var(--brand-blue); line-height: 1;
  }
  .salutation {
    position: absolute; left: 54px; top: 210px;
    font-size: 25px; font-weight: 600; color: var(--brand-blue);
  }
  .letter-body {
    position: absolute; left: 54px; top: 250px; width: 660px;
    font-size: 18px; line-height: 26px; color: var(--ink);
    text-align: justify; letter-spacing: -0.2px;
  }
  .letter-body p + p { margin-top: 26px; }
  .sign-off {
    position: absolute; left: 542px; top: 730px;
    color: var(--ink-soft);
  }
  .sign-name { font-size: 11px; }
  .sign-title { font-size: 9px; margin-top: 2px; }
  .signature-area {
    position: absolute; left: 535px; top: 755px;
    width: 168px; height: 82px;
    background: linear-gradient(135deg, var(--paper), var(--sig-tone), var(--paper));
  }
  .contact {
    position: absolute; left: 56px; top: 906px;
    list-style: none; font-size: 18px; color: var(--ink);
  }
  .contact li { display: flex; align-items: flex-start; gap: 8px; line-height: 20px; margin-bottom: 5px; }
  .contact svg { flex: none; margin-top: 2px; }
  .contact .address svg { margin-top: 8px; }
  .footer-band { position: absolute; left: 0; bottom: 0; width: 768px; height: 50px; }
  .website {
    position: absolute; right: 83px; bottom: 12px;
    font-size: 25px; letter-spacing: 2px; color: var(--paper);
  }
</style>
</head>
<body>
<main class="letterhead">
  <header class="brand">
    <span class="brand-mark"></span>
    <span class="brand-name">PEXUMOR LABS</span>
  </header>

  <h1 class="salutation">Dear Mr. John,</h1>

  <section class="letter-body">
    <p>Lorem ipsum dolor sit amet, consectetuer adipiscing elit, sed diam nonummy nibh euismod tincidunt ut laoreet dolore magna aliquam erat volutpat. Ut wisi enim ad minim veniam, quis nostrud exerci tation ullamcorper suscipit lobortis nisl ut aliquip ex ea commodo consequat. Duis autem vel eum iriure dolor in hendrerit in vulputate velit esse molestie consequat, vel illum dolore eu feugiat nulla facilisis at vero eros et accumsan et iusto odio dignissim qui blandit praesent luptatum zzril delenit augue duis dolore te feugait nulla facilisi.</p>
    <p>Lorem ipsum dolor sit amet, cons ectetuer adipiscing elit, sed diam nonummy nibh euismod tincidunt ut laoreet dolore magna aliquam erat volutpat. Ut wisi Lorem ipsum dolor sit amet, consectetuer adipiscing elit, sed diam nonummy nibh euismod tincidunt ut laoreet dolore magna aliquam erat volutpat. Ut wisi enim ad minim veniam, quis nostrud exerci tation ullamcorper suscipit lobortis nisl ut aliquip ex ea commodo consequat. Duis autem vel eum iriure dolor in hendrerit in vulputate velit esse molestie consequat,Lorem ipsum dolor sit amet, cons ectetuer adipiscing elit, sed diam nonummy nibh euismod tincidunt ut laoreet dolore magna aliquam erat volutpat.</p>
  </section>

  <div class="sign-off">
    <div class="sign-name">John Doe</div>
    <div class="sign-title">Office Maneger</div>
  </div>
  <div class="signature-area" role="img" aria-label="Handwritten signature"></div>

  <ul class="contact">
    <li>
      <svg width="18" height="18" viewBox="0 0 24 24"><path fill="var(--brand-orange)" d="M6.6 10.8a15 15 0 0 0 6.6 6.6l2.2-2.2a1 1 0 0 1 1-.25 11.4 11.4 0 0 0 3.6.57 1 1 0 0 1 1 1V20a1 1 0 0 1-1 1A17 17 0 0 1 3 4a1 1 0 0 1 1-1h3.5a1 1 0 0 1 1 1c0 1.25.2 2.45.57 3.57a1 1 0 0 1-.25 1z"/></svg>
      <span>(602)-417-3926</span>
    </li>
    <li>
      <svg width="18" height="18" viewBox="0 0 24 24"><rect x="2" y="5" width="20" height="14" fill="var(--brand-orange)"/><path d="M2 5l10 8 10-8M2 19l7-6M22 19l-7-6" stroke="#fff" stroke-width="1.6" fill="none"/></svg>
      <span>information@pexumor.com</span>
    </li>
    <li class="address">
      <svg width="18" height="22" viewBox="0 0 24 30"><path d="M12 2a9 9 0 0 0-9 9c0 7 9 17 9 17s9-10 9-17a9 9 0 0 0-9-9z" fill="none" stroke="var(--brand-orange)" stroke-width="3"/><circle cx="12" cy="11" r="3" fill="var(--brand-orange)"/></svg>
      <span>4817 N. Corwin Street<br>Phoenix, AZ 85021</span>
    </li>
  </ul>

  <svg class="footer-band" viewBox="0 0 768 50" preserveAspectRatio="none">
    <path d="M0 22 H360 C380 22 388 20 398 16 L380 16 C372 18 366 19 355 19 H0 Z" fill="var(--brand-orange)"/>
    <path d="M0 29 H355 C375 29 390 27 405 20 C425 10 440 6 470 6 H768 V50 H0 Z" fill="var(--brand-blue)"/>
  </svg>
  <div class="website">www.pexumor.com</div>
</main>
</body>
</html>
```